Design business cards for Ironvale Barbers (Opening March so won't need finalised till January2018

Ironvale Barbers is the new age barbers and skincare for all men. Creating tailor made haircuts & customised skincare solutions for the perfect healthy manly look. The Barbers will have a industrial, rustic, worldly feel about it. Rustic red brick wall with old wine barrels as the work stations with the old fashion barber chairs. Concrete floor and a bit corrugated iron around.
Target Market(s)
Professional males who like a great haircut, wet shave and may consider a facial if in the right environment. Total pampering experience in a boys environment.
Industry/Entity Type
Barber
Contact Information for Business Card
Front- Logo - address is 42 Kowhai Rd Taupo
Ph - (07) 548 9163
www.ironvalebarbers.com
email - hello@ironvale.co.nz
Back of card
Mens Haircare - Wet Shaving - Facials - Skin Prescriptions
We are doing a loyalty program - 6 squares numbered then 7th free
Colors
Designer to choose colors to be used in the design.
Requirements
Must have
- Clean simple easy to read.
Nice to have
- Our current colours are white font on black background but thinking we need to introduce another colour. Maybe white logo on a copper, bronze or rusty background. Or even a rustic red brick wall with white writing. Want it clean simple to read. Maybe a burgundy?
Should not have
- no images like heads, scissors, razors please

```html
<!DOCTYPE html>
<html lang="en">
<head>
<meta charset="utf-8">
<title>Ironvale Barbers – Business Cards</title>
<link href="https://fonts.googleapis.com/css2?family=Cinzel:wght@700&family=Open+Sans:wght@400&display=swap" rel="stylesheet">
<style>
  :root {
    --backdrop: #3a3330;
    --card-black: #0d0d0d;
    --ink-white: #f4f4f4;
    --ink-silver: #c9c9c9;
    --band-grey: #e3e3e3;
    --ink-dark: #2a2a2a;
  }
  html, body {
    margin: 0;
    width: 1200px;
    height: 900px;
    overflow: hidden;
    background: var(--backdrop);
  }
  .canvas {
    position: relative;
    width: 1200px;
    height: 900px;
  }
  .card {
    position: absolute;
    top: 300px;
    width: 525px;
    height: 300px;
    background: var(--card-black);
    box-shadow: 0 10px 30px rgba(0,0,0,0.45);
    overflow: hidden;
  }
  .card--front { left: 50px; }
  .card--back { left: 625px; }

  .brand {
    font-family: "Cinzel", serif;
    font-weight: 700;
    color: var(--ink-white);
    text-align: center;
    line-height: 1;
  }
  .brand__name { display: block; font-size: 40px; letter-spacing: 1px; }
  .brand__sub { display: block; font-size: 16px; letter-spacing: 6px; margin-top: 4px; }

  .card--front .brand {
    position: absolute;
    top: 42px;
    right: 36px;
  }

  .contact-list {
    position: absolute;
    left: 30px;
    bottom: 28px;
    margin: 0;
    padding: 0;
    list-style: none;
    font-family: "Open Sans", sans-serif;
    font-size: 16px;
    color: var(--ink-white);
  }
  .contact-list li {
    display: flex;
    align-items: center;
    gap: 10px;
    height: 24px;
  }
  .contact-list li.contact--address { margin-top: 14px; }
  .contact-list svg { width: 14px; height: 14px; flex: none; }

  .card--back .brand {
    position: absolute;
    top: 38px;
    left: 0;
    right: 0;
    color: var(--ink-silver);
  }
  .services {
    position: absolute;
    top: 136px;
    left: 0;
    right: 0;
    text-align: center;
    font-family: "Cinzel", serif;
    font-weight: 700;
    font-size: 10.5px;
    letter-spacing: 0.6px;
    color: var(--ink-silver);
  }
  .appointment-band {
    position: absolute;
    left: 0;
    right: 0;
    bottom: 0;
    height: 118px;
    background: var(--band-grey);
  }
  .appointment-fields {
    position: absolute;
    left: 34px;
    right: 34px;
    top: 52px;
    display: flex;
    gap: 14px;
    font-family: "Cinzel", serif;
    font-weight: 700;
    font-size: 12px;
    color: var(--ink-dark);
  }
  .field { display: flex; align-items: flex-end; gap: 6px; flex: 1; }
  .field__line { flex: 1; border-bottom: 1px solid var(--ink-dark); height: 12px; }
</style>
</head>
<body>
<div class="canvas">

  <section class="card card--front" aria-label="Front of business card">
    <div class="brand">
      <span class="brand__name">IRONVALE</span>
      <span class="brand__sub">BARBERS</span>
    </div>
    <ul class="contact-list">
      <li>
        <svg viewBox="0 0 24 24" aria-hidden="true"><path fill="#f4f4f4" d="M6.6 10.8a15.1 15.1 0 0 0 6.6 6.6l2.2-2.2c.3-.3.7-.4 1-.2 1.1.4 2.3.6 3.6.6.6 0 1 .4 1 1V20c0 .6-.4 1-1 1A17 17 0 0 1 3 4c0-.6.4-1 1-1h3.5c.6 0 1 .4 1 1 0 1.3.2 2.5.6 3.6.1.3 0 .7-.2 1z"/></svg>
        (07) 548 9163
      </li>
      <li>
        <svg viewBox="0 0 24 24" aria-hidden="true"><rect x="2" y="5" width="20" height="14" rx="1" fill="#f4f4f4"/><path d="M3 6l9 7 9-7" stroke="#0d0d0d" stroke-width="2" fill="none"/></svg>
        hello@ironvale.co.nz
      </li>
      <li>
        <svg viewBox="0 0 24 24" aria-hidden="true"><circle cx="12" cy="12" r="10" fill="#f4f4f4"/><path d="M2 12h20M12 2c3 3 3 17 0 20M12 2c-3 3-3 17 0 20" stroke="#0d0d0d" stroke-width="1.5" fill="none"/></svg>
        www.ironvalebarbers.com
      </li>
      <li class="contact--address">
        <svg viewBox="0 0 24 24" aria-hidden="true"><path fill="#f4f4f4" d="M12 2a7 7 0 0 0-7 7c0 5 7 13 7 13s7-8 7-13a7 7 0 0 0-7-7zm0 9.5a2.5 2.5 0 1 1 0-5 2.5 2.5 0 0 1 0 5z"/></svg>
        42 Kowhai Rd Taupo
      </li>
    </ul>
  </section>

  <section class="card card--back" aria-label="Back of business card">
    <div class="brand">
      <span class="brand__name">IRONVALE</span>
      <span class="brand__sub">BARBERS</span>
    </div>
    <p class="services">MENS HAIRCARE | WET SHAVING | FACIALS | SKIN PRESCRIPTIONS</p>
    <div class="appointment-band">
      <div class="appointment-fields">
        <div class="field"><span>DATE:</span><span class="field__line"></span></div>
        <div class="field"><span>TIME:</span><span class="field__line"></span></div>
      </div>
    </div>
  </section>

</div>
</body>
</html>
```